Notary Signing Agent Need Business card Design

Need a Business card design for my new company. RT Velo-Brisk LLC
Mobile Notary Signing Agent. I go to the customer for closing of Mortgage's Documents . possible signs of honesty, integrity and confidentiality.

Work with Title company to Notary Mortgage closing.

My Target Market is Title companies. Banks and Financial Institution.

Color Blue to Black Professional ) if needed some Green Little Red

And possible a company logo.

Mobile ( travel to clients ) Integrity, Honest Trustworthy. A show of Professional services.

Would like company name and my name on card

Use both sides and front with business name and my name. phone numbers.

Target Market(s)

Title company, Banks mortgage company

Industry/Entity Type

Travel

Contact Information for Business Card

Notary, Certified signing agent, Mobile

Colors
0455a3

Requirements
Must have
• Name of company , owners name phone number,
Nice to have
• blue and black color like a professional look but not limit to these only.
• a stand out from other cards .

```html
<!DOCTYPE html>
<html lang="en">
<head>
<meta charset="utf-8">
<title>RT Velo-Brisk LLC — Business Card</title>
<link rel="stylesheet" href="https://fonts.googleapis.com/css2?family=Michroma&display=swap">
<style>
  :root {
    --brand-blue: #0a6fb5;
    --accent-blue: #1596d6;
    --accent-green: #b8d43a;
    --card-black: #0c0d0f;
    --card-black-soft: #17191c;
    --page-white: #ffffff;
    --band-dark: #111213;
    --band-light: #4a4a4a;
  }
  * { margin: 0; padding: 0; box-sizing: border-box; }
  html, body { width: 1200px; height: 1047px; overflow: hidden; }
  body {
    position: relative;
    background: var(--page-white);
    font-family: "Michroma", "Arial", sans-serif;
  }
  .card {
    position: absolute;
    width: 500px;
    height: 286px;
    border-radius: 18px;
    overflow: hidden;
    background: radial-gradient(ellipse at 50% 45%, var(--card-black-soft), var(--card-black) 75%);
    box-shadow: 0 4px 10px rgba(0,0,0,0.35);
  }
  .card-front { left: 60px; top: 250px; }
  .card-back  { left: 640px; top: 250px; }
  .card-edges { position: absolute; inset: 0; width: 100%; height: 100%; }

  .wordmark {
    position: absolute;
    color: var(--brand-blue);
    text-transform: uppercase;
    letter-spacing: 2px;
    line-height: 1.3;
    display: flex;
    align-items: center;
    gap: 12px;
    white-space: nowrap;
  }
  .wordmark-square {
    width: 18px; height: 18px;
    background: var(--brand-blue);
    flex: none;
  }
  .card-front .wordmark {
    left: 30px; top: 122px;
    width: 200px;
    font-size: 11px;
    letter-spacing: 1px;
    gap: 10px;
  }
  .card-front .wordmark-square { width: 14px; height: 14px; }
  .card-back .wordmark  { left: 0; right: 0; top: 118px; justify-content: center; font-size: 24px; }

  .divider {
    position: absolute;
    left: 248px; top: 88px;
    width: 2px; height: 118px;
    background: var(--accent-blue);
  }
  .contact {
    position: absolute;
    left: 272px; top: 104px;
    color: var(--accent-blue);
    text-transform: uppercase;
    white-space: nowrap;
  }
  .contact-name { font-size: 13px; letter-spacing: 2px; margin-bottom: 10px; }
  .contact-line {
    display: flex; align-items: center; gap: 8px;
    font-size: 11px; letter-spacing: 4px; margin-bottom: 6px;
  }
  .contact-line svg { width: 12px; height: 13px; flex: none; }

  .logo-band {
    position: absolute;
    left: 0; top: 778px;
    width: 1200px; height: 269px;
    background: linear-gradient(90deg, var(--band-dark) 0%, var(--band-dark) 55%, var(--band-light) 100%);
  }
  .logo-band .wordmark {
    left: 46px; top: 100px;
    font-size: 44px;
    letter-spacing: 3px;
    gap: 20px;
  }
  .logo-band .wordmark-square { width: 44px; height: 44px; }
</style>
</head>
<body>

  <section class="card card-front" aria-label="Business card front">
    <svg class="card-edges" viewBox="0 0 500 286" preserveAspectRatio="none" aria-hidden="true">
      <polygon points="240,0 500,0 500,58" fill="var(--brand-blue)"/>
      <line x1="240" y1="0" x2="500" y2="58" stroke="var(--accent-green)" stroke-width="1.5"/>
      <polygon points="0,226 0,286 270,286" fill="var(--brand-blue)"/>
      <line x1="0" y1="226" x2="270" y2="286" stroke="var(--accent-green)" stroke-width="1.5"/>
    </svg>
    <div class="wordmark"><span class="wordmark-square"></span><span>RT<br>Velo-Brisk LLC</span></div>
    <div class="divider"></div>
    <div class="contact">
      <p class="contact-name">Daniel R Hollis</p>
      <p class="contact-line">
        <svg viewBox="0 0 12 13" aria-hidden="true"><rect x="2.5" y="0.5" width="7" height="12" rx="1.5" fill="none" stroke="currentColor"/><rect x="5" y="10" width="2" height="1" fill="currentColor"/></svg>
        555-014-2736
      </p>
      <p class="contact-line">
        <svg viewBox="0 0 12 13" aria-hidden="true"><rect x="0.5" y="4" width="11" height="8" rx="1" fill="currentColor"/><rect x="3" y="0.5" width="6" height="4" fill="none" stroke="currentColor"/></svg>
        555-019-4820
      </p>
    </div>
  </section>

  <section class="card card-back" aria-label="Business card back">
    <svg class="card-edges" viewBox="0 0 500 286" preserveAspectRatio="none" aria-hidden="true">
      <polygon points="230,0 500,0 500,60" fill="var(--brand-blue)"/>
      <line x1="230" y1="0" x2="500" y2="60" stroke="var(--accent-green)" stroke-width="1.5"/>
    </svg>
    <div class="wordmark"><span class="wordmark-square"></span><span>RT Velo-Brisk LLC</span></div>
  </section>

  <section class="logo-band" aria-label="Company name lockup">
    <div class="wordmark"><span class="wordmark-square"></span><span>RT<br>Velo-Brisk LLC</span></div>
  </section>

</body>
</html>
```